Mirabo & Orvan Automotive Repair Shop. Need a new website design.

We specialize in Mirabo & Orvan auto repair, but also work on other Asian import vehicles. We have been in business for 7 years and pride ourselves on high quality auto repair that is fixed right the first time. Would like the automotive repair website to incorporate the colors black, red and white if possible and have our logo and some Mirabo and Orvan vehicles included in the website.

Target Market(s)

Mirabo & Orvan vehicle owners

Industry/Entity Type

Automotive Repair

Coding

Coded - Design and coding required

Number of Pages Required

5+ page

Colors
EB3D1F
EC4F4E
F09395
F8D3D4
FCEDEE

Requirements
Must have
• Home, Services, Contact Us, Schedule appointment, and a gallery tab that I can add shop pictures to when completed.
Nice to have
• Would like to see example pictures of job next to each service listed.
Should not have
• Service not related to auto repair. Ex. auto detailing, towing, car wash

```html
<!DOCTYPE html>
<html lang="en">
<head>
<meta charset="utf-8">
<title>Dunmore Automotive – Mirabo &amp; Orvan Auto Repair</title>
<link rel="stylesheet" href="https://fonts.googleapis.com/css2?family=Michroma&family=Barlow:wght@400;500;600;700&display=swap">
<style>
:root{
  --red:#e1161e;
  --red-dark:#b10e14;
  --black:#0b0b0b;
  --ink:#141414;
  --panel:#1a1a1a;
  --grey:#8c8c8c;
  --line:#4a4a4a;
  --white:#ffffff;
  --soft:#d4d4d4;
}
*{box-sizing:border-box;margin:0;padding:0}
html,body{width:1200px;height:4743px;overflow:hidden;background:var(--black)}
body{position:relative;font-family:'Barlow',sans-serif;color:var(--white)}
.section{position:absolute;left:0;width:1200px;overflow:hidden}
.abs{position:absolute}
.display{font-family:'Michroma',sans-serif;text-transform:uppercase;letter-spacing:2px}
.eyebrow{font-family:'Michroma',sans-serif;font-size:12px;color:var(--red);text-transform:uppercase;letter-spacing:1px}
.btn{position:absolute;display:flex;align-items:center;justify-content:center;font-weight:700;text-transform:uppercase;font-size:15px}
.btn-red{background:var(--red);color:var(--white)}
.btn-outline{border:2px solid var(--soft);color:var(--white);font-size:13px;letter-spacing:1px}
.center{text-align:center;left:0;width:1200px}

/* header */
.site-header{top:0;height:150px;z-index:5}
.brand{left:140px;top:22px;width:155px;height:120px;display:flex;align-items:center;justify-content:center;gap:8px}
.brand .dot{width:14px;height:14px;background:var(--red);border-radius:50%}
.brand span{font-weight:700;font-size:22px;line-height:1}
.nav a{position:absolute;top:50px;font-size:13px;font-weight:500;color:var(--white);text-decoration:none;text-transform:uppercase}
.nav a.active::after{content:"";position:absolute;left:0;right:0;bottom:-10px;height:2px;background:var(--red)}
.nav .finance{left:841px;top:40px;width:171px;height:37px;border:2px solid var(--soft);display:flex;align-items:center;justify-content:center;font-size:11px;font-weight:600}
.award{left:1032px;top:22px;width:76px;height:76px;border-radius:50%;border:3px solid #2e4a5a;background:#16232b}

/* hero */
.hero{top:0;height:760px;background:linear-gradient(180deg,#151515,#0b0b0b)}
.hero-photo{left:440px;top:130px;width:760px;height:560px;background:linear-gradient(115deg,#0f0f0f 0%,#3a3a3a 35%,#8e8e8e 60%,#4a4a4a 85%,#1b1b1b 100%)}
.hero-frame{left:131px;top:221px;width:110px;height:313px;border:4px solid #555;border-right:none}
.hero h1{left:176px;top:266px;font-size:31px;line-height:40px;font-weight:400}
.hero h1 .accent{color:var(--red)}
.hero .tagline{left:178px;top:390px;font-size:22px;font-weight:500}
.hero .btn{left:180px;top:442px;width:282px;height:51px;font-size:15px}

/* about */
.about{top:755px;height:535px;background:#0d0d0d}
.about-mark{left:115px;top:60px;width:450px;height:370px;display:flex;align-items:center;justify-content:center;gap:16px}
.about-mark .dot{width:40px;height:40px;background:var(--red);border-radius:50%}
.about-mark span{font-weight:700;font-size:52px}
.about .eyebrow{left:609px;top:42px}
.about h2{left:609px;top:68px;font-size:30px}
.about .lead{left:612px;top:122px;width:520px;font-size:16px;line-height:24px;font-weight:600}
.about .body{left:612px;top:205px;width:520px;font-size:15px;line-height:23px;color:var(--soft)}
.about .btn{left:618px;top:417px;width:166px;height:46px}

/* services */
.services{top:1288px;height:740px;background:radial-gradient(ellipse at 50% 40%,#222,#121212 70%)}
.services .eyebrow{top:62px}
.services h2{top:86px;font-size:29px}
.svc-col{position:absolute;top:165px;list-style:none;display:flex;flex-direction:column}
.svc-col li{display:flex;align-items:center;gap:14px;min-height:46px;padding:5px 0;font-size:14px;font-weight:600;text-transform:uppercase;line-height:22px}
.svc-col li svg{flex:none;width:30px;height:30px}
.svc-col li.active{background:var(--red);clip-path:polygon(0 0,100% 0,93% 100%,0 100%);margin-left:-25px;padding-left:25px;width:284px}
.band{position:absolute;left:0;width:1200px}

/* gallery */
.gallery{top:1895px;height:860px;background:linear-gradient(180deg,#1c1c1c,#0f0f0f)}
.gallery .eyebrow{top:186px}
.gallery h2{top:212px;font-size:29px}
.shot{position:absolute}
.shot-a{background:linear-gradient(135deg,#4a4a4a,#1e1e1e 60%,#6b5a3c)}
.shot-b{background:linear-gradient(160deg,#9c9c9c,#3c3c3c 55%,#141414)}
.shot-c{background:linear-gradient(135deg,#4a6f8a,#8a8a8a 50%,#2b2b2b)}
.shot-d{background:linear-gradient(180deg,#6a6a6a,#b9b9b9 45%,#2a3a70)}
.shot-e{background:linear-gradient(180deg,#6c5b4a,#3a3a3a 40%,#1f1f1f)}

/* makes */
.makes{top:2751px;height:620px;background:#0c0c0c}
.makes h2{top:65px;font-size:20px;line-height:25px}
.make-grid{position:absolute;left:131px;top:178px;width:920px;height:287px;display:grid;grid-template-columns:repeat(4,1fr);grid-template-rows:repeat(2,1fr);border:1px solid var(--line)}
.make-grid div{border:1px solid var(--line);display:flex;align-items:center;justify-content:center;gap:10px;font-weight:600;font-size:22px;letter-spacing:3px;text-transform:uppercase}
.make-grid div.lit{background:linear-gradient(135deg,#f2f2f2,#9a9a9a);color:#111}
.makes .btn{left:447px;top:517px;width:291px;height:55px;font-size:18px}

/* testimonials */
.reviews{top:3367px;height:435px;background:radial-gradient(ellipse at 50% 50%,#1e1e1e,#0f0f0f 75%)}
.reviews .eyebrow{top:46px}
.reviews h2{top:73px;font-size:29px}
.card{position:absolute;top:138px;width:400px;height:197px;border:2px solid #444;text-align:center;padding:28px 40px 0}
.card .q{color:var(--red);font-family:'Michroma',sans-serif;font-size:40px;line-height:30px;height:34px}
.card p{font-size:15px;line-height:27px;color:var(--soft);margin-top:6px}
.card h4{font-size:15px;font-weight:700;margin-top:14px}

/* contact */
.contact{top:3800px;height:610px;background:linear-gradient(90deg,#161616,#262626 50%,#151515)}
.contact .eyebrow{left:132px;top:95px}
.contact h2{left:132px;top:128px;font-size:31px}
.contact h2 .accent{color:var(--red)}
.contact .rule{left:40px;top:113px;width:70px;height:2px;background:#444}
.contact .rule::after{content:"";position:absolute;right:-2px;top:-2px;width:6px;height:6px;background:var(--red)}
.contact .intro{left:132px;top:175px;width:395px;font-size:15px;line-height:27px;color:var(--soft)}
.info{position:absolute;left:135px;display:flex;align-items:center;gap:15px;font-size:15px;line-height:27px}
.info .ic{width:32px;height:32px;border-radius:50%;background:#d9d9d9;display:flex;align-items:center;justify-content:center;flex:none}
.form{left:593px;top:86px;width:491px;height:346px;border:2px solid #3a3a3a;background:rgba(10,10,10,.55)}
.form h3{position:absolute;left:40px;top:35px;font-size:15px}
.field{position:absolute;border:1px solid #666;font-size:10px;font-weight:600;padding:8px 14px}
.form .btn{left:40px;top:270px;width:132px;height:37px;font-family:'Michroma',sans-serif;font-size:11px}

/* footer */
.footer{top:4330px;height:413px;background:#0c0c0c}
.footer-brand{left:520px;top:20px;width:160px;height:120px;display:flex;align-items:center;justify-content:center;gap:8px;z-index:2}
.footer-brand .dot{width:12px;height:12px;background:var(--red);border-radius:50%}
.footer-brand span{font-weight:700;font-size:20px}
.footer-nav a{position:absolute;top:166px;font-size:16px;font-weight:700;color:var(--white);text-decoration:none;text-transform:uppercase}
.footer-nav i{position:absolute;top:174px;width:5px;height:5px;background:var(--red)}
.copy{left:175px;top:218px;font-size:12px}
.social{position:absolute;top:215px;width:22px;height:22px;border:2px solid var(--white);border-radius:50%}
.partner{position:absolute;top:275px;height:60px;display:flex;align-items:center;justify-content:center;font-weight:700;font-size:22px}
</style>
</head>
<body>

<!-- HERO -->
<section class="section hero">
  <div class="abs hero-photo" role="img" aria-label="Mechanic working on an exposed engine block"></div>
  <div class="abs" style="left:0;top:130px;width:700px;height:560px;background:linear-gradient(90deg,#121212 55%,rgba(18,18,18,0))"></div>
  <div class="abs hero-frame"></div>
  <h1 class="abs display">Specializing in<br>Mirabo and Orvan<br><span class="accent">Auto Repair</span></h1>
  <p class="abs tagline">Dealership Quality at an affordable price.</p>
  <a class="btn btn-red">Schedule an Appointment</a>
  <svg class="abs" style="left:0;top:600px" width="1200" height="160" viewBox="0 0 1200 160">
    <polygon points="0,145 560,95 1200,40 1200,160 0,160" fill="#0d0d0d"/>
    <polygon points="0,130 560,82 1200,24 1200,44 560,100 0,152" fill="var(--red)"/>
  </svg>
</section>

<!-- HEADER -->
<header class="section site-header">
  <div class="abs brand"><i class="dot"></i><span>DUNMORE</span></div>
  <nav class="nav">
    <a class="active" style="left:361px">Home</a>
    <a style="left:438px">About Us</a>
    <a style="left:546px">Services</a>
    <a style="left:653px">Gallery</a>
    <a style="left:754px">Contact</a>
    <a class="finance">Financing Application</a>
  </nav>
  <div class="abs award"></div>
</header>

<!-- ABOUT -->
<section class="section about">
  <div class="abs about-mark"><i class="dot"></i><span>DUNMORE</span></div>
  <p class="abs eyebrow">Our Company</p>
  <h2 class="abs display">About Dunmore</h2>
  <svg class="abs" style="left:965px;top:78px" width="170" height="8"><rect x="0" y="1" width="8" height="6" fill="#999"/><rect x="10" y="3.5" width="160" height="1" fill="#444"/></svg>
  <p class="abs lead">Dunmore Automotive is a locally owned and operated auto repair shop in Fairhaven that offers comprehensive car care and services for Mirabo &amp; Orvan and all other Asian imports vehicles.</p>
  <p class="abs body">Led by an NMT master certified technician with 20 years experience working for Mirabo &amp; Orvan dealerships, our auto shop is your go to facility for everything from factory auto maintenance, including oil changes, fluid services and tune ups, to complex engine repairs, hybrid diagnostic &amp; repair, brake jobs, etc. We have state of the art equipment and tools to ensure that we can properly diagnose and repair your vehicle to get you back on the road quickly. Our work comes with a warranty and we offer towing if needed. We also offer discounts for RideGo &amp; Hopp rides.</p>
  <a class="btn btn-outline" style="left:618px;top:417px;width:166px;height:46px">Learn More</a>
</section>

<!-- SERVICES -->
<section class="section services">
  <p class="abs eyebrow center">What We Do</p>
  <h2 class="abs display center">Services Provide</h2>
  <svg width="0" height="0" style="position:absolute">
    <defs>
      <g id="svc-icon"><circle cx="15" cy="15" r="11" fill="none" stroke="#fff" stroke-width="2"/><circle cx="15" cy="15" r="4" fill="#fff"/></g>
    </defs>
  </svg>
  <ul class="svc-col" style="left:123px">
    <li class="active"><svg viewBox="0 0 30 30"><use href="#svc-icon"/></svg>Oil Changes</li>
    <li><svg viewBox="0 0 30 30"><use href="#svc-icon"/></svg>Computer Diagnostics</li>
    <li><svg viewBox="0 0 30 30"><use href="#svc-icon"/></svg>Electrical Specialists</li>
    <li><svg viewBox="0 0 30 30"><use href="#svc-icon"/></svg>Tires</li>
    <li><svg viewBox="0 0 30 30"><use href="#svc-icon"/></svg>Tire Balance &amp; Rotations</li>
    <li><svg viewBox="0 0 30 30"><use href="#svc-icon"/></svg>Pre Purchase Inspections</li>
    <li><svg viewBox="0 0 30 30"><use href="#svc-icon"/></svg>Insurance Claims</li>
    <li><svg viewBox="0 0 30 30"><use href="#svc-icon"/></svg>Emission Repair &amp; Catalytic<br>Converters</li>
  </ul>
  <ul class="svc-col" style="left:429px">
    <li><svg viewBox="0 0 30 30"><use href="#svc-icon"/></svg>Engine Repair</li>
    <li><svg viewBox="0 0 30 30"><use href="#svc-icon"/></svg>Heating &amp; AC Repair</li>
    <li><svg viewBox="0 0 30 30"><use href="#svc-icon"/></svg>State Inspection</li>
    <li><svg viewBox="0 0 30 30"><use href="#svc-icon"/></svg>Suspension Service &amp; Repair</li>
    <li><svg viewBox="0 0 30 30"><use href="#svc-icon"/></svg>Leveling Kits &amp; Minor Lift Kit<br>Installation</li>
    <li><svg viewBox="0 0 30 30"><use href="#svc-icon"/></svg>Brakes Service &amp; Repair</li>
    <li><svg viewBox="0 0 30 30"><use href="#svc-icon"/></svg>Exhaust, Muffler Service &amp; Repair</li>
    <li><svg viewBox="0 0 30 30"><use href="#svc-icon"/></svg>Automatic, Manual, Computerized<br>Transmission Service &amp; Repair</li>
  </ul>
  <ul class="svc-col" style="left:796px">
    <li><svg viewBox="0 0 30 30"><use href="#svc-icon"/></svg>Clutch Service &amp; Repair</li>
    <li><svg viewBox="0 0 30 30"><use href="#svc-icon"/></svg>CV Axle Service &amp; Repair</li>
    <li><svg viewBox="0 0 30 30"><use href="#svc-icon"/></svg>Fuel Injection System Service<br>Cleaning &amp; Repair</li>
    <li><svg viewBox="0 0 30 30"><use href="#svc-icon"/></svg>Timing Belts &amp; Water Pumps</li>
    <li><svg viewBox="0 0 30 30"><use href="#svc-icon"/></svg>Radiators &amp; Fans Service &amp; Repair</li>
    <li><svg viewBox="0 0 30 30"><use href="#svc-icon"/></svg>Tune Ups &amp; Factory Scheduled<br>Maintenance</li>
    <li><svg viewBox="0 0 30 30"><use href="#svc-icon"/></svg>Hybrid Vehicle Diagnostic &amp; Repair<br>24-HR Night Drop</li>
  </ul>
</section>

<!-- GALLERY -->
<section class="section gallery">
  <svg class="band" style="top:0" width="1200" height="140" viewBox="0 0 1200 140">
    <polygon points="0,0 1200,0 1200,0 600,110 0,0" fill="#131313"/>
    <polygon points="0,0 600,110 1200,0 1200,22 600,130 0,22" fill="#8a8a8a"/>
  </svg>
  <p class="abs eyebrow center">Photo Gallery</p>
  <h2 class="abs display center">Our Gallery</h2>
  <div class="shot shot-a" style="left:107px;top:282px;width:324px;height:235px" role="img" aria-label="Technician working under a lifted vehicle"></div>
  <div class="shot shot-b" style="left:442px;top:282px;width:324px;height:235px" role="img" aria-label="Front of an SUV with the hood open"></div>
  <div class="shot shot-c" style="left:777px;top:282px;width:324px;height:235px" role="img" aria-label="Engine bay with components removed"></div>
  <div class="shot shot-d" style="left:110px;top:536px;width:488px;height:235px" role="img" aria-label="Silver pickup truck on a service lift"></div>
  <div class="shot shot-e" style="left:611px;top:536px;width:490px;height:235px" role="img" aria-label="Row of SUVs parked outside the shop"></div>
</section>

<!-- MAKES -->
<section class="section makes">
  <h2 class="abs display center">Dunmore Automotive specializes in Mirabo &amp; Orvan<br>auto repair but also service and repair<br>the following makes</h2>
  <div class="make-grid">
    <div>Arvane</div>
    <div>Hollin</div>
    <div>Inverro</div>
    <div>Kessa</div>
    <div class="lit">Mirrow</div>
    <div>Mazeno</div>
    <div>Norvik</div>
    <div>Hadrel</div>
  </div>
  <a class="btn btn-red">Financing Application</a>
</section>

<!-- TESTIMONIALS -->
<section class="section reviews">
  <p class="abs eyebrow center">Reviews</p>
  <h2 class="abs display center">Testimonials</h2>
  <article class="card" style="left:191px">
    <div class="q">"</div>
    <p>I would highly recommend Dunmore Automotive to family, friends, &amp; co-workers! I'm a repeat customer myself!</p>
    <h4>DANIEL R.</h4>
  </article>
  <article class="card" style="left:613px">
    <div class="q">"</div>
    <p>Dunmore Automotive is my go to car repair company. I trust them with all my vehicle needs.</p>
    <h4>PRIYA S.</h4>
  </article>
</section>

<!-- CONTACT -->
<section class="section contact">
  <div class="abs rule"></div>
  <p class="abs eyebrow">Get in Touch</p>
  <h2 class="abs display">Contact <span class="accent">Us</span></h2>
  <p class="abs intro">Contact us for a free estimate! Please include year, make, and model and the service or repair you would like repair you would like an estimate on.</p>
  <div class="info" style="top:268px">
    <span class="ic"><svg width="16" height="12" viewBox="0 0 16 12"><rect x="1" y="1" width="14" height="10" fill="none" stroke="#222" stroke-width="1.6"/><path d="M1 1l7 6 7-6" fill="none" stroke="#222" stroke-width="1.6"/></svg></span>
    hello@dunmoreauto.example</div>
  <div class="info" style="top:323px">
    <span class="ic"><svg width="16" height="16" viewBox="0 0 16 16"><path d="M3 1l3 3-2 2c1 2 3 4 5 5l2-2 3 3-2 3C7 15 1 9 1 3z" fill="#222"/></svg></span>
    <span>OFFICE. 555.013.9110<br>CELL. 555.289.7493</span></div>
  <div class="info" style="top:399px">
    <span class="ic"><svg width="16" height="16" viewBox="0 0 16 16"><circle cx="8" cy="8" r="6.5" fill="none" stroke="#222" stroke-width="1.6"/><path d="M8 4v4l3 2" fill="none" stroke="#222" stroke-width="1.6"/></svg></span>
    Mon to Fri 8.30 am to 6 pm</div>
  <div class="abs form">
    <h3 class="display">Leave us a message</h3>
    <div class="field" style="left:40px;top:77px;width:201px;height:37px">First Name*</div>
    <div class="field" style="left:250px;top:77px;width:202px;height:37px">Last Name*</div>
    <div class="field" style="left:40px;top:127px;width:201px;height:37px">Email address*</div>
    <div class="field" style="left:250px;top:127px;width:202px;height:37px">Phone*</div>
    <div class="field" style="left:40px;top:177px;width:412px;height:81px">Message</div>
    <a class="btn btn-red">Submit</a>
  </div>
</section>

<!-- FOOTER -->
<footer class="section footer">
  <svg class="band" style="top:0" width="1200" height="100" viewBox="0 0 1200 100">
    <polygon points="0,70 600,0 1200,70 1200,0 0,0" fill="#1e1e1e"/>
    <polygon points="0,62 600,2 1200,62 1200,82 600,22 0,82" fill="#8a8a8a"/>
  </svg>
  <div class="abs footer-brand"><i class="dot"></i><span>DUNMORE</span></div>
  <nav class="footer-nav">
    <a style="left:168px">Home</a><i style="left:274px"></i>
    <a style="left:328px">About Us</a><i style="left:469px"></i>
    <a style="left:519px">Our Services</a><i style="left:694px"></i>
    <a style="left:746px">Gallery</a><i style="left:873px"></i>
    <a style="left:931px">Contact</a>
  </nav>
  <p class="abs copy">Copyright © 2024 Dunmore Automotive. All rights reserved.</p>
  <span class="social" style="left:878px"></span>
  <span class="social" style="left:913px"></span>
  <span class="social" style="left:948px"></span>
  <span class="social" style="left:983px"></span>
  <div class="partner" style="left:180px;width:150px">Stateline Cells</div>
  <div class="partner" style="left:400px;width:150px">Torqol</div>
  <div class="partner" style="left:650px;width:56px"><span style="width:56px;height:76px;background:#1f3f8c;border:3px solid #d0d0d0"></span></div>
  <div class="partner" style="left:820px;width:180px">Easyplan</div>
</footer>

</body>
</html>
```